Accounting and Financial Services Firm - Modern, Fresh, Original, Professional

We need a business card designed. We would like to see use of the the colors blue. Logo attached.

Modern, Fresh, Original, Professional,
Updates

Email section on business card required. design brief updated.

Target Market(s)

Small to medium businesses and high net worth individuals

Industry/Entity Type

Public Accounting

Contact Information for Business Card

Business Name: PL Ledgerworth Chartered Accountants
Address: Level 9, 42 Garnet Lane Sydney NSW 2000
Ph: 02 9314 2758
Mobile: 04 XXXX XXXX
Email: mara@plledgerworth.com.au
Wechat ID: XXXXXXX
Website: www.plledgerworth.com.au

Name: Mara Osei
Position: Manager

Font styles to use
Sans Serif

Colors
0492cd
33a6d7
85cae6

Requirements
Must have
• Modern font.

```html
<!DOCTYPE html>
<html lang="en">
<head>
<meta charset="utf-8">
<title>PL Ledgerworth — Business Card</title>
<link rel="stylesheet" href="https://fonts.googleapis.com/css2?family=Source+Sans+3:ital,wght@0,300;0,400;0,600;1,400&display=swap">
<style>
  :root {
    --page-bg: #e4e5e7;
    --card-black: #0a0a0b;
    --brand-blue: #0492cd;
    --brand-blue-mid: #33a6d7;
    --brand-blue-light: #85cae6;
    --band-blue: #0a82bf;
    --rule-grey: #8b9096;
    --text-grey: #a7abb0;
    --back-deep: #03345f;
    --back-glow: #0a9be0;
    --white: #ffffff;
  }
  * { box-sizing: border-box; margin: 0; padding: 0; }
  html, body {
    width: 1200px; height: 1200px; overflow: hidden;
    background: var(--page-bg);
    font-family: "Source Sans 3", "Helvetica Neue", Arial, sans-serif;
  }
  .sheet {
    width: 1200px; height: 1200px;
    display: flex; flex-direction: column; align-items: center; justify-content: center;
    gap: 52px;
  }
  .card {
    position: relative;
    width: 900px; height: 514px;
    border-radius: 6px;
    overflow: hidden;
    box-shadow: 0 10px 30px rgba(0,0,0,.18);
  }

  /* Front side */
  .card--front { background: var(--card-black); }
  .card__band { position: absolute; inset: 0; width: 100%; height: 100%; }
  .holder { position: absolute; left: 96px; top: 50px; }
  .holder__name {
    font-size: 40px; font-weight: 400; font-style: italic;
    color: var(--brand-blue); text-transform: uppercase; letter-spacing: .5px;
    line-height: 1;
  }
  .holder__role { margin-top: 6px; font-size: 18px; font-style: italic; color: var(--text-grey); }
  .contact { position: absolute; left: 96px; top: 150px; color: var(--text-grey); font-size: 18px; line-height: 1.3; }
  .contact__address { margin-bottom: 12px; }
  .contact__list { list-style: none; }
  .contact__item { display: flex; align-items: center; gap: 12px; height: 28px; }
  .contact__icon { width: 19px; height: 19px; flex: none; }
  .brand-mark {
    position: absolute; right: 56px; top: 238px;
    display: flex; align-items: flex-start; gap: 16px;
    color: var(--brand-blue); font-weight: 600;
  }
  .brand-mark__name { font-size: 44px; line-height: 1; letter-spacing: 1px; text-transform: uppercase; }
  .brand-mark__tag { font-size: 14px; letter-spacing: 4.4px; text-transform: uppercase; margin-top: 8px; }
  .brand-mark__square { width: 54px; height: 54px; background: var(--brand-blue); flex: none; margin-top: -34px; }

  /* Back side */
  .card--back {
    background: radial-gradient(ellipse 62% 70% at 52% 42%, var(--back-glow) 0%, #0670b0 40%, var(--back-deep) 100%);
    color: var(--white);
    display: flex; flex-direction: column; align-items: center; justify-content: center;
  }
  .back-brand { text-align: center; font-weight: 600; }
  .back-brand__name { font-size: 68px; line-height: 1; letter-spacing: 2px; text-transform: uppercase; }
  .back-brand__tag { font-size: 20px; letter-spacing: 8px; text-transform: uppercase; margin-top: 8px; }
  .back-site { margin-top: 46px; font-size: 28px; font-weight: 600; letter-spacing: 1px; }
</style>
</head>
<body>
<main class="sheet">

  <section class="card card--front" aria-label="Business card front">
    <svg class="card__band" viewBox="0 0 900 514" preserveAspectRatio="none" aria-hidden="true">
      <path d="M0,380 L590,458" stroke="var(--rule-grey)" stroke-width="8" fill="none"/>
      <path d="M0,394 L585,470 Q596,472 606,464 Q614,458 628,460 L900,496 L900,514 L0,514 Z" fill="var(--band-blue)"/>
    </svg>

    <div class="holder">
      <h1 class="holder__name">Mara Osei</h1>
      <p class="holder__role">Manager</p>
    </div>

    <div class="contact">
      <p class="contact__address">Level 9, 42 Garnet Lane<br>Sydney NSW 2000</p>
      <ul class="contact__list">
        <li class="contact__item">
          <svg class="contact__icon" viewBox="0 0 20 20" aria-hidden="true"><ellipse cx="8" cy="8" rx="7" ry="5.5" fill="var(--brand-blue)"/><ellipse cx="13" cy="12.5" rx="6" ry="4.5" fill="var(--brand-blue-mid)"/></svg>
          XXXXXXX
        </li>
        <li class="contact__item">
          <svg class="contact__icon" viewBox="0 0 20 20" aria-hidden="true"><rect x="5" y="1" width="10" height="18" rx="2" fill="var(--brand-blue)"/><rect x="7" y="4" width="6" height="9" fill="var(--card-black)"/></svg>
          04 XXXX XXXX
        </li>
        <li class="contact__item">
          <svg class="contact__icon" viewBox="0 0 20 20" aria-hidden="true"><path d="M2,7 Q10,1 18,7 L16,9 L13,7.5 L13,6 Q10,5 7,6 L7,7.5 L4,9 Z" fill="var(--brand-blue)"/><rect x="4" y="11" width="12" height="7" rx="1.5" fill="var(--brand-blue)"/></svg>
          02 9314 2758
        </li>
        <li class="contact__item">
          <svg class="contact__icon" viewBox="0 0 20 20" aria-hidden="true"><rect x="1.5" y="4" width="17" height="12" rx="1.5" fill="none" stroke="var(--brand-blue)" stroke-width="2"/><path d="M2,5 L10,11 L18,5" fill="none" stroke="var(--brand-blue)" stroke-width="2"/></svg>
          mara@plledgerworth.com.au
        </li>
        <li class="contact__item">
          <svg class="contact__icon" viewBox="0 0 20 20" aria-hidden="true"><circle cx="10" cy="10" r="8" fill="none" stroke="var(--brand-blue)" stroke-width="2"/><path d="M2,10 H18 M10,2 Q5,10 10,18 M10,2 Q15,10 10,18" stroke="var(--brand-blue)" stroke-width="1.5" fill="none"/></svg>
          www.plledgerworth.com.au
        </li>
      </ul>
    </div>

    <div class="brand-mark">
      <div class="brand-mark__text">
        <p class="brand-mark__name">PL Ledgerworth</p>
        <p class="brand-mark__tag">Chartered Accountants</p>
      </div>
      <span class="brand-mark__square" aria-hidden="true"></span>
    </div>
  </section>

  <section class="card card--back" aria-label="Business card back">
    <div class="back-brand">
      <p class="back-brand__name">PL Ledgerworth</p>
      <p class="back-brand__tag">Chartered Accountants</p>
    </div>
    <p class="back-site">www.plledgerworth.com.au</p>
  </section>

</main>
</body>
</html>
```